Menubook for a 2star restaurant

Hey,
We are looking for a new menu for a 2 star restaurant in Belgium. They want a clean, abstract, with small light accents of gold, copper. The format will be 21 cm by 21 cm. and the booklet will have 4 printable sides inc front & back. Only the logo on the front. The wine list will be separate so it should not be included in the design. "Bites" - "voorgerechten" - "hoofdgerechten" & "nagerechten" must be copied.

Industry/Entity Type

Restaurant

Requirements
Must have
• Clean look
Nice to have
• touches of gold

```html
<!DOCTYPE html>
<html lang="nl">
<head>
<meta charset="utf-8">
<title>Menukaart – Hoofdgerechten &amp; Nagerechten</title>
<link rel="stylesheet" href="https://fonts.googleapis.com/css2?family=Arvo:ital,wght@0,400;1,400&display=swap">
<style>
  :root {
    --mustard: #dcb51f;
    --ink: #1b1407;
    --heading: #eaf6dc;
    --band: #0b0908;
  }
  html, body { margin: 0; padding: 0; overflow: hidden; }
  body { width: 1200px; height: 1200px; background: var(--band); font-family: "Arvo", serif; }
  .page { position: relative; width: 1200px; height: 1200px; overflow: hidden; background: var(--band); }

  .photo { position: absolute; }
  .photo--main-dish {
    left: 814px; top: 0; width: 386px; height: 748px;
    background:
      radial-gradient(ellipse 70% 40% at 60% 25%, #d9c98a 0%, #b99a55 45%, transparent 75%),
      radial-gradient(ellipse 60% 30% at 45% 55%, #8a4a2a 0%, transparent 70%),
      radial-gradient(ellipse 90% 25% at 70% 92%, #a2243e 0%, transparent 70%),
      linear-gradient(180deg, #4a1c1c 0%, #3a1518 60%, #2a0f12 100%);
  }
  .photo--bruschetta {
    left: 0; top: 775px; width: 1200px; height: 425px;
    background:
      radial-gradient(ellipse 35% 55% at 45% 50%, #e2493c 0%, #c9302a 45%, transparent 80%),
      radial-gradient(ellipse 25% 40% at 12% 85%, #3f6a2c 0%, transparent 75%),
      radial-gradient(ellipse 30% 40% at 85% 95%, #c98a55 0%, transparent 75%),
      linear-gradient(90deg, #b7a8b3 0%, #c95045 30%, #d6453a 55%, #b85a40 80%, #9a6a4a 100%);
  }

  .panel { position: absolute; background: var(--mustard); color: var(--ink); }
  .panel--mains { left: 0; top: 0; width: 814px; height: 748px; }
  .panel--desserts { left: 628px; top: 775px; width: 572px; height: 277px; }

  .section-title {
    position: absolute; margin: 0; font-weight: 400; color: var(--heading);
    font-size: 47px; line-height: 1; letter-spacing: 0.5px;
  }
  .panel--mains .section-title { left: 67px; top: 42px; }
  .panel--desserts .section-title { left: 28px; top: 49px; }

  .row { position: absolute; display: flex; justify-content: space-between; font-size: 17.5px; line-height: 1; white-space: nowrap; }
  .panel--mains .row { left: 67px; width: 695px; }
  .panel--desserts .row { left: 28px; width: 496px; font-size: 17px; }
  .dish { text-transform: uppercase; }
  .detail { font-style: italic; }
</style>
</head>
<body>
<div class="page">
  <div class="photo photo--main-dish" role="img" aria-label="Gegratineerd gerecht met kaas en basilicum in een rode schaal"></div>
  <div class="photo photo--bruschetta" role="img" aria-label="Bruschetta met tomaat en kruiden naast sla"></div>

  <section class="panel panel--mains">
    <h2 class="section-title">HOOFDGERECHTEN</h2>
    <div class="row dish" style="top:111px"><span>Spaghetti Vongole *</span><span>29</span></div>
    <div class="row detail" style="top:160px"><span>bosui | piemento | zilte groenten</span></div>
    <div class="row dish" style="top:208px"><span>Kabeljauw Rug *</span><span>36</span></div>
    <div class="row detail" style="top:257px"><span>limoen | kappertjes | mosselen | safraan</span></div>
    <div class="row dish" style="top:305px"><span>Kalfsfilet *</span><span>46</span></div>
    <div class="row detail" style="top:353px"><span>paarse bloemkool | girolle | groen asperge | daslook | pijpajuin</span></div>
    <div class="row dish" style="top:402px"><span>Insalate del Giorno</span></div>
    <div class="row" style="top:450px"><span>vlees of vis</span><span>40</span></div>
    <div class="row" style="top:499px"><span>veggie</span><span>33</span></div>
    <div class="row dish" style="top:547px"><span>Gnocchi</span><span>29</span></div>
    <div class="row detail" style="top:596px"><span>salie | spinazie | barilotto</span></div>
    <div class="row dish" style="top:644px"><span>Gepocheerd Hoeve Ei</span><span>36</span></div>
    <div class="row detail" style="top:692px"><span>girolle | daslook | groene asperges</span></div>
  </section>

  <section class="panel panel--desserts">
    <h2 class="section-title">NAGERECHTEN</h2>
    <div class="row dish" style="top:114px"><span>Assortiment van 5 Italiaanse kazen</span><span>27</span></div>
    <div class="row dish" style="top:163px"><span>Amalfi citroen met meringue *</span><span>16</span></div>
    <div class="row dish" style="top:211px"><span>* Menu | 5 gangen</span><span>95</span></div>
  </section>
</div>
</body>
</html>
```